Graphic Design - Website Header - Leaderboard

Hello,
I am looking for a design to go above the navigation on my website/blog. Design will include an image, name of website and some followup wording or taglines.

Website will be a wordpress blog about mens lifestyle, but will be more rugged in nature, the anti-VX blog for men. A man's man blog - think Tarnwell Rider image. Inspiring young men about women, whiskey, boots, jeans & proper manners .. that sort of thing. Want to appeal to cosmopolitan men .. not actual cowboys, so no cowboy hats.

Would like an image on the left of the face of a tough looking, handsome man, looking into the page, with scruff. Man must be a drawing or abstract image, no photo.

Image should be at least 900 x 200 pixels and use earth tones. Navigation under image will be something like - About, Lifestyle, Attire, Transport, Man Skills, Booze, Women, Contact.

Name of blog will be TheFlintBrow.example
Updates

Serious about a legit design .. cmon people . this is an easy one ...please read my detailed brief.  Let me know if you have questions.... and, THANK YOU !

Reason: still looking for designs .. very detailed specs in the brief Thank You !

Target Market(s)

23-40yr old men, looking for tips on how to look and act like a cool guy and appeal to women

Industry/Entity Type

Graphic Design

Requirements
Must have
• 1. Drawing of a Man with scruff on left side of graphic, looking into the page (to the right). Not a photograph - an image or drawing. See uploaded image - want something ssimilar in style.

2. Masculine Earth Tones & Fonts. textured background

3. Include name of site in middle ..with tagline below it
"Guiding Gents Through Boots, Bourbon & Good Graces"
(ability to easily change the tagline)
Nice to have
• Ability to easily use this design on a business card
Should not have
• 1. Actual photo of man
2. Shirtless guy
3. Cowboy hat or cigarette

```html
<!DOCTYPE html>
<html lang="en">
<head>
<meta charset="utf-8">
<title>The Flint Brow – Leaderboard Header</title>
<link href="https://fonts.googleapis.com/css2?family=Alfa+Slab+One&family=PT+Sans:wght@400&display=swap" rel="stylesheet">
<style>
  :root {
    --stage: #0b0204;
    --stage-glow: #140608;
    --paper: #eeeae4;
    --paper-warm: #e3dccf;
    --grunge: #8c6c48;
    --grunge-dark: #5a4028;
    --ink: #2a1411;
  }
  html, body {
    margin: 0;
    padding: 0;
    width: 1200px;
    height: 1000px;
    overflow: hidden;
    background: var(--stage);
  }
  .canvas {
    position: relative;
    width: 1200px;
    height: 1000px;
    background: var(--stage);
  }
  .backdrop-figure {
    position: absolute;
    left: 360px;
    top: 60px;
    width: 380px;
    height: 356px;
    border-radius: 48% 48% 30% 30%;
    background: radial-gradient(ellipse at 50% 45%, var(--stage-glow) 0%, var(--stage) 70%);
  }
  .leaderboard {
    position: absolute;
    left: 110px;
    top: 416px;
    width: 980px;
    height: 168px;
    overflow: hidden;
    background: radial-gradient(ellipse at 50% 45%, var(--paper) 55%, var(--paper-warm) 100%);
  }
  .leaderboard-texture {
    position: absolute;
    inset: 0;
  }
  .portrait {
    position: absolute;
    left: 0;
    top: 6px;
    width: 138px;
    height: 162px;
    background: linear-gradient(160deg, #5a4a44 0%, var(--ink) 60%, #1a0c0a 100%);
    border-radius: 46% 40% 0 0;
  }
  .title {
    position: absolute;
    left: 171px;
    top: 30px;
    width: 700px;
    margin: 0;
    text-align: center;
    font-family: "Alfa Slab One", serif;
    font-weight: 400;
    font-size: 64px;
    line-height: 1;
    font-variant: small-caps;
    letter-spacing: 2px;
    color: var(--ink);
    white-space: nowrap;
  }
  .tagline-rule {
    position: absolute;
    top: 112px;
    height: 6px;
    background: var(--ink);
  }
  .tagline-rule.left { left: 118px; width: 115px; }
  .tagline-rule.right { left: 820px; width: 148px; }
  .tagline {
    position: absolute;
    left: 240px;
    top: 103px;
    width: 570px;
    margin: 0;
    text-align: center;
    font-family: "PT Sans", sans-serif;
    font-size: 20px;
    line-height: 24px;
    letter-spacing: 0.3px;
    color: var(--ink);
    white-space: nowrap;
  }
  .site-url {
    position: absolute;
    right: 22px;
    top: 136px;
    margin: 0;
    font-family: "Alfa Slab One", serif;
    font-size: 15px;
    line-height: 18px;
    font-variant: small-caps;
    color: var(--ink);
    white-space: nowrap;
  }
</style>
</head>
<body>
<div class="canvas">
  <div class="backdrop-figure" role="img" aria-label="Faint dark silhouette of a man's head in profile"></div>

  <header class="leaderboard">
    <svg class="leaderboard-texture" width="980" height="168" viewBox="0 0 980 168" aria-hidden="true">
      <rect x="0" y="0" width="980" height="14" fill="var(--grunge)" opacity="0.75"/>
      <rect x="0" y="12" width="980" height="3" fill="var(--grunge-dark)" opacity="0.5"/>
      <rect x="6" y="18" width="968" height="140" fill="none" stroke="var(--grunge)" stroke-width="1.5" opacity="0.5"/>
      <rect x="0" y="150" width="980" height="18" fill="var(--grunge)" opacity="0.35"/>
      <rect x="0" y="0" width="6" height="168" fill="var(--grunge)" opacity="0.4"/>
      <rect x="974" y="0" width="6" height="168" fill="var(--grunge)" opacity="0.4"/>
    </svg>

    <div class="portrait" role="img" aria-label="Drawn portrait of a scruffy man in sunglasses looking to the right"></div>

    <h1 class="title">The Flint Brow</h1>

    <span class="tagline-rule left"></span>
    <p class="tagline">Guiding Gents Through Boots, Bourbon &amp; Good Graces</p>
    <span class="tagline-rule right"></span>

    <p class="site-url">TheFlintBrow.example</p>
  </header>
</div>
</body>
</html>
```